Banner ads for Bidspots

Need 6 banners for virus removal software. Banners will be the same design just different dimensions.

Target Market(s)

People who own PC's that are infected with a virus. They are looking to remove the virus.

Requirements
Must have
• Requirements:
• 1. 6 banners in the following sizes
• 336x280
• 250x250
• 300x250
• 200x200
• 120x600
• 160x600
• 2. Banners in French. Just use Google Translate. We will fix Grammar
• 3. Target a specific virus threat called "Zel4"
• 4. Images must be 150 KB or smaller
• 5. Banners must follow bidspots image ad policies on https://help.norvanta-example.com/bidspotspolicy/answer/482913?ctx=image&hl=en
• The idea is for us to easily be able to swap out the name of the virus with a new virus threat.
Nice to have
• Special notice will go to those who can do some animation. Just ensure it follows the bidspots policies. An Example banner a while back I liked bounced down then rotated one direction and then rotated another direction. It caught the eye very well. If I recall correctly it was a porn banner. We are going for getting noticed on a webpage for high Click Through Rates.

```html
<!DOCTYPE html>
<html lang="fr">
<head>
<meta charset="utf-8">
<title>Bannières Bidspots – Supprimer les virus Zel4</title>
<link rel="stylesheet" href="https://fonts.googleapis.com/css2?family=Lato:wght@700;900&family=Russo+One&family=Lora:wght@500&display=swap">
<style>
  :root {
    --board: #222222;
    --label: #f2f2f2;
    --field: #f1f1f1;
    --plum-dark: #6c2352;
    --plum: #8e2d6e;
    --plum-light: #c45a9f;
    --head-top: #c03f9a;
    --head-bottom: #7e1f62;
    --button-top: #86346c;
    --button-bottom: #5d1c46;
    --virus-core: #d36bb4;
    --virus-edge: rgba(241, 241, 241, 0);
  }
  * { box-sizing: border-box; margin: 0; padding: 0; }
  html, body { width: 1200px; height: 1000px; overflow: hidden; background: var(--board); }
  .board { position: relative; width: 1200px; height: 1000px; }

  .size-label {
    position: absolute;
    font-family: "Lato", sans-serif;
    font-weight: 700;
    font-size: 26px;
    color: var(--label);
    text-align: center;
    transform: translateX(-50%);
    white-space: nowrap;
  }

  .banner {
    position: absolute;
    overflow: hidden;
    background: linear-gradient(90deg, var(--plum-dark), var(--plum-light) 50%, var(--plum-dark));
  }
  .banner__field {
    position: absolute;
    left: -20%;
    right: -20%;
    top: 0;
    background: var(--field);
  }
  .banner__art {
    position: absolute;
    left: 0;
    right: 0;
    background:
      radial-gradient(ellipse at 50% 45%, var(--virus-core) 0%, rgba(200, 80, 160, 0.45) 35%, var(--virus-edge) 72%);
  }
  .banner__headline {
    position: absolute;
    left: 0;
    right: 0;
    font-family: "Russo One", sans-serif;
    text-align: center;
    text-transform: uppercase;
    background: linear-gradient(180deg, var(--head-top), var(--head-bottom));
    -webkit-background-clip: text;
    background-clip: text;
    color: transparent;
    letter-spacing: 0.5px;
  }
  .banner__button {
    position: absolute;
    left: 50%;
    transform: translateX(-50%);
    display: flex;
    align-items: center;
    justify-content: center;
    border-radius: 5px;
    background: linear-gradient(180deg, var(--button-top), var(--button-bottom));
    font-family: "Lora", serif;
    font-weight: 500;
    color: #ffffff;
    white-space: nowrap;
  }

  /* 336 x 280 */
  .banner--336 { left: 62px; top: 80px; width: 335px; height: 280px; }
  .banner--336 .banner__field { height: 265px; border-radius: 0 0 50% 50% / 0 0 42px 42px; }
  .banner--336 .banner__art { top: 0; height: 110px; }
  .banner--336 .banner__headline { top: 114px; font-size: 29px; line-height: 38px; }
  .banner--336 .banner__button { top: 203px; width: 179px; height: 37px; font-size: 19px; }

  /* 300 x 250 */
  .banner--300 { left: 80px; top: 406px; width: 300px; height: 250px; }
  .banner--300 .banner__field { height: 238px; border-radius: 0 0 50% 50% / 0 0 34px 34px; }
  .banner--300 .banner__art { top: 0; height: 88px; }
  .banner--300 .banner__headline { top: 101px; font-size: 26px; line-height: 35px; }
  .banner--300 .banner__button { top: 182px; width: 151px; height: 32px; font-size: 17px; }

  /* 250 x 250 */
  .banner--250 { left: 105px; top: 717px; width: 250px; height: 250px; }
  .banner--250 .banner__field { height: 238px; border-radius: 0 0 50% 50% / 0 0 20px 20px; }
  .banner--250 .banner__art { top: 0; height: 90px; }
  .banner--250 .banner__headline { top: 104px; font-size: 23px; line-height: 30px; }
  .banner--250 .banner__button { top: 173px; width: 164px; height: 33px; font-size: 17px; }

  /* 200 x 200 */
  .banner--200 { left: 515px; top: 420px; width: 200px; height: 200px; }
  .banner--200 .banner__field { height: 190px; border-radius: 0 0 50% 50% / 0 0 18px 18px; }
  .banner--200 .banner__art { top: 0; height: 56px; }
  .banner--200 .banner__headline { top: 79px; font-size: 17.5px; line-height: 25px; }
  .banner--200 .banner__button { top: 136px; width: 136px; height: 27px; font-size: 14px; }

  /* 160 x 600 */
  .banner--160 { left: 825px; top: 208px; width: 160px; height: 600px; }
  .banner--160 .banner__field { top: 45px; height: 520px; border-radius: 50% 50% 50% 50% / 22px 22px 22px 22px; }
  .banner--160 .banner__art--top { top: 72px; height: 140px; }
  .banner--160 .banner__art--bottom { top: 385px; height: 150px; }
  .banner--160 .banner__headline { top: 240px; font-size: 18px; line-height: 27px; }
  .banner--160 .banner__button { top: 329px; width: 134px; height: 27px; font-size: 14px; }

  /* 120 x 600 */
  .banner--120 { left: 1034px; top: 208px; width: 120px; height: 600px; }
  .banner--120 .banner__field { top: 45px; height: 520px; border-radius: 50% 50% 50% 50% / 18px 18px 18px 18px; }
  .banner--120 .banner__art--top { top: 72px; height: 140px; }
  .banner--120 .banner__art--bottom { top: 385px; height: 150px; }
  .banner--120 .banner__headline { top: 253px; font-size: 15px; line-height: 22px; }
  .banner--120 .banner__button { top: 325px; width: 110px; height: 24px; font-size: 12px; }
</style>
</head>
<body>
<main class="board">

  <div class="size-label" style="left:229px; top:42px;">336x280</div>
  <section class="banner banner--336">
    <div class="banner__field"></div>
    <div class="banner__art" role="img" aria-label="Rangée de virus violets à pointes"></div>
    <h2 class="banner__headline">Supprimer<br>les virus Zel4</h2>
    <div class="banner__button">Telecharger</div>
  </section>

  <div class="size-label" style="left:230px; top:368px;">300x250</div>
  <section class="banner banner--300">
    <div class="banner__field"></div>
    <div class="banner__art" role="img" aria-label="Rangée de virus violets à pointes"></div>
    <h2 class="banner__headline">Supprimer<br>les virus Zel4</h2>
    <div class="banner__button">Telecharger</div>
  </section>

  <div class="size-label" style="left:230px; top:677px;">250x250</div>
  <section class="banner banner--250">
    <div class="banner__field"></div>
    <div class="banner__art" role="img" aria-label="Rangée de virus violets à pointes"></div>
    <h2 class="banner__headline">Supprimer<br>les virus Zel4</h2>
    <div class="banner__button">Telecharger</div>
  </section>

  <div class="size-label" style="left:615px; top:380px;">200x200</div>
  <section class="banner banner--200">
    <div class="banner__field"></div>
    <div class="banner__art" role="img" aria-label="Rangée de virus violets à pointes"></div>
    <h2 class="banner__headline">Supprimer<br>les virus Zel4</h2>
    <div class="banner__button">Telecharger</div>
  </section>

  <div class="size-label" style="left:905px; top:168px;">160x600</div>
  <section class="banner banner--160">
    <div class="banner__field"></div>
    <div class="banner__art banner__art--top" role="img" aria-label="Groupe de virus violets à pointes"></div>
    <h2 class="banner__headline">Supprimer<br>les virus<br>Zel4</h2>
    <div class="banner__button">Telecharger</div>
    <div class="banner__art banner__art--bottom" role="img" aria-label="Groupe de virus violets à pointes"></div>
  </section>

  <div class="size-label" style="left:1094px; top:168px;">120x600</div>
  <section class="banner banner--120">
    <div class="banner__field"></div>
    <div class="banner__art banner__art--top" role="img" aria-label="Groupe de virus violets à pointes"></div>
    <h2 class="banner__headline">Supprimer<br>les virus<br>Zel4</h2>
    <div class="banner__button">Telecharger</div>
    <div class="banner__art banner__art--bottom" role="img" aria-label="Groupe de virus violets à pointes"></div>
  </section>

</main>
</body>
</html>
```